Startup internet service provider needs a good facebook ad

Looking for a catchy facebook ad to launch our internet service in Parker, Colorado. Short video or slideshow preferred, still pictures are okay.

https://www.facebook.com/BrimfoxNetworks

www.brimfox-networks.example

Target Market(s)

Parker Colorado

Colors
add136
0255a3

```html
<!DOCTYPE html>
<html lang="en">
<head>
<meta charset="utf-8">
<title>Brimfox Networks – Fast and Reliable Internet Service</title>
<link rel="stylesheet" href="https://fonts.googleapis.com/css2?family=Poppins:wght@300;400;500;600;700;800&display=swap">
<style>
  :root {
    --brand-green: #add136;
    --brand-blue: #0255a3;
    --text-dark: #2f2f33;
    --text-body: #3a3a3f;
    --page-bg: #dcdcdc;
    --card-bg: #ffffff;
  }
  * { box-sizing: border-box; margin: 0; padding: 0; }
  html, body {
    width: 1200px; height: 1200px; overflow: hidden;
    background: linear-gradient(180deg, #e6e6e6 0%, var(--page-bg) 100%);
    font-family: "Poppins", sans-serif;
  }
  .ad-card {
    position: absolute; left: 50px; top: 230px;
    width: 1100px; height: 741px;
    background: linear-gradient(180deg, var(--card-bg) 55%, #f0f1f3 100%);
    overflow: hidden;
  }
  .brand {
    position: absolute; left: 50px; top: 44px;
    display: flex; align-items: center; gap: 12px;
  }
  .brand-dot {
    width: 40px; height: 40px; border-radius: 50%;
    background: var(--brand-blue);
  }
  .brand-name {
    font-weight: 500; font-size: 27px; color: var(--brand-blue);
    letter-spacing: 0.2px;
  }
  .headline {
    position: absolute; left: 47px; top: 118px;
    line-height: 0.9;
  }
  .headline .big {
    font-weight: 800; color: var(--brand-green);
    font-size: 83px; letter-spacing: -0.5px;
  }
  .headline .and {
    font-weight: 400; color: var(--text-dark);
    font-size: 42px; margin-left: 6px;
  }
  .service-band {
    position: absolute; left: 49px; top: 275px;
    width: 348px; height: 44px;
    background: var(--brand-blue); color: #fff;
    font-weight: 400; font-size: 30px; line-height: 44px;
    text-align: center; letter-spacing: 0.3px;
  }
  .subhead {
    position: absolute; left: 49px; top: 336px;
    font-size: 19px; line-height: 27px; font-weight: 400;
    color: var(--text-body); letter-spacing: 0.2px;
  }
  .feature-list {
    position: absolute; left: 49px; top: 408px;
    list-style: none;
  }
  .feature-list li {
    display: flex; align-items: center; gap: 12px;
    font-size: 15.5px; height: 23px; color: var(--text-body);
  }
  .feature-list svg { width: 12px; height: 12px; flex: none; }
  .photo-circle {
    position: absolute; left: 476px; top: 18px;
    width: 604px; height: 604px; border-radius: 50%;
    background: radial-gradient(circle at 50% 55%, #e9d6c6 0%, #b9c7d6 55%, #5e7fa6 100%);
  }
  .contact-bar {
    position: absolute; left: 0; bottom: 0;
    width: 1100px; height: 104px;
    background: var(--brand-blue);
  }
  .call-label {
    position: absolute; left: 49px; top: 18px;
    font-weight: 600; font-size: 17px; color: var(--brand-green);
  }
  .phone-number {
    position: absolute; left: 46px; top: 30px;
    font-weight: 600; font-size: 58px; color: #fff; letter-spacing: 0.5px;
  }
  .web-pill {
    position: absolute; left: 499px; top: 0;
    width: 601px; height: 104px;
    background: linear-gradient(90deg, #b9d93e 0%, var(--brand-green) 100%);
    border-radius: 52px 0 0 52px;
    display: flex; align-items: center; padding-left: 38px; gap: 22px;
  }
  .web-icon {
    width: 52px; height: 52px; border-radius: 50%; background: #fff;
    display: flex; align-items: center; justify-content: center; flex: none;
  }
  .web-address {
    font-weight: 700; font-size: 27px; color: #fff;
  }
  .web-address .tld { font-weight: 400; }
</style>
</head>
<body>
  <main class="ad-card">
    <div class="brand">
      <span class="brand-dot"></span>
      <span class="brand-name">Brimfox Networks</span>
    </div>

    <h1 class="headline">
      <span class="big">FAST</span><span class="and">AND</span><br>
      <span class="big">RELIABLE</span>
    </h1>

    <div class="service-band">INTERNET SERVICE</div>

    <p class="subhead">DESIGNED AND CATERED TO MEET<br>YOUR NEEDS</p>

    <ul class="feature-list">
      <li><svg viewBox="0 0 12 12"><path d="M1 6.5 L4.5 10 L11 2.5" fill="none" stroke="#add136" stroke-width="2"/></svg>Fast and reliable internet service</li>
      <li><svg viewBox="0 0 12 12"><path d="M1 6.5 L4.5 10 L11 2.5" fill="none" stroke="#add136" stroke-width="2"/></svg>Real customer support</li>
      <li><svg viewBox="0 0 12 12"><path d="M1 6.5 L4.5 10 L11 2.5" fill="none" stroke="#add136" stroke-width="2"/></svg>Less buffering while streaming</li>
      <li><svg viewBox="0 0 12 12"><path d="M1 6.5 L4.5 10 L11 2.5" fill="none" stroke="#add136" stroke-width="2"/></svg>Fast web browsing</li>
      <li><svg viewBox="0 0 12 12"><path d="M1 6.5 L4.5 10 L11 2.5" fill="none" stroke="#add136" stroke-width="2"/></svg>Gaming without the lag</li>
      <li><svg viewBox="0 0 12 12"><path d="M1 6.5 L4.5 10 L11 2.5" fill="none" stroke="#add136" stroke-width="2"/></svg>Wall to wall WiFi coverage</li>
      <li><svg viewBox="0 0 12 12"><path d="M1 6.5 L4.5 10 L11 2.5" fill="none" stroke="#add136" stroke-width="2"/></svg>No introductory charges, one constant rate</li>
      <li><svg viewBox="0 0 12 12"><path d="M1 6.5 L4.5 10 L11 2.5" fill="none" stroke="#add136" stroke-width="2"/></svg>Simple and easy to read bills</li>
    </ul>

    <div class="photo-circle" role="img" aria-label="Photo of a family on a sofa using a tablet, a phone and a laptop together"></div>

    <footer class="contact-bar">
      <div class="call-label">CALL US TOLL FREE</div>
      <div class="phone-number">844-555-0172</div>
      <div class="web-pill">
        <span class="web-icon">
          <svg width="30" height="30" viewBox="0 0 30 30" fill="none" stroke="#add136" stroke-width="1.8">
            <circle cx="15" cy="15" r="12"/>
            <ellipse cx="15" cy="15" rx="5.5" ry="12"/>
            <path d="M3 15 H27 M5 9 H25 M5 21 H25"/>
          </svg>
        </span>
        <span class="web-address">brimfox-networks<span class="tld">.example</span></span>
      </div>
    </footer>
  </main>
</body>
</html>
```